Flat Belly Design Graphics for Social

I want to create 9 social media graphics (new Instagram size 4:5 (1080 x 1350 pixels) focusing on our Flat Belly Graphics, using the pics attached. Use the attached pics, NO RANDOM STOCK PHOTOGRAPHY. For the color scheme of the graphics, the color palette is attached. YOU MUST POST ALL 9 GRAPHICS IN ONE ENTRY.
Using the 3 titles below, create one set of graphics. 1) with all text, then for the others, use the pictures as detailed below in IMPORTANT:
1. 21-Night Lean Middle Reboot Beyond 50
2. The 20-Second Trim-Core Menu Guide
3. Starlet Tricks to a Slender Midline Beyond 50 - Zero Scalpel Needed
IMPORTANT:
Only use RK Pic 1 and RK Pic 2 with the title, 21-Night Lean Middle Reboot Beyond 50
Only use meal plan1 and meal plan2 pics with the title, 20-Second Trim-Core Menu Guide
Only use starlet tricks 1 and starlet tricks 2 pics with the title, Starlet Tricks to a Slender Midline Beyond 50 - Zero Scalpel Needed
women over 40

```html
<!DOCTYPE html>
<html lang="en">
<head>
<meta charset="utf-8">
<title>Lean Middle Reboot – Social Grid</title>
<link href="https://fonts.googleapis.com/css2?family=Bebas+Neue&family=Montserrat:wght@800;900&family=Raleway:wght@700&display=swap" rel="stylesheet">
<style>
  :root{
    --forest:#2f4d4b;
    --rose:#e497b0;
    --blush:#f8cddb;
    --blush-soft:#fbe1ea;
    --white:#ffffff;
  }
  *{box-sizing:border-box;margin:0;padding:0}
  html,body{width:960px;height:1200px;overflow:hidden;background:var(--white)}
  .grid{position:relative;width:960px;height:1200px;background:var(--white)}
  .tile{position:absolute;overflow:hidden}
  .col-1{left:0;width:309px}
  .col-2{left:325px;width:311px}
  .col-3{left:652px;width:308px}
  .row-1{top:0;height:394px}
  .row-2{top:410px;height:384px}
  .row-3{top:810px;height:390px}
  .tile svg.backdrop{position:absolute;inset:0;width:100%;height:100%}
  .photo{position:absolute}
  .photo-portrait{inset:0;background:linear-gradient(160deg,#f6c3d4 0%,#e9a6bd 40%,#5b3a30 75%,#1c1a1a 100%)}
  .photo-kitchen{inset:0;background:linear-gradient(160deg,#6b4634 0%,#b98a6e 35%,#efe7e4 60%,#1f1e1f 100%)}
  .photo-friends{inset:0;background:linear-gradient(150deg,#3a514f 0%,#c99b86 45%,#efd2c6 70%,#8fb6d0 100%)}
  .photo-friends-alt{left:0;top:0;width:100%;height:249px;background:linear-gradient(150deg,#f7d6e0 0%,#c48e72 45%,#3a2620 70%,#f2ece9 100%)}

  /* Title card */
  .title-card{position:absolute;left:13px;top:14px;width:284px;height:374px}
  .title-card .top{position:absolute;left:0;top:0;width:100%;height:172px;background:var(--white)}
  .title-card .bottom{position:absolute;left:0;top:172px;width:100%;height:202px;background:var(--forest)}
  .title-card .dots{position:absolute;inset:9px;border:3px dotted var(--forest)}
  .title-card .bottom-dots{position:absolute;left:9px;right:9px;top:0;bottom:9px;border:3px dotted var(--white);border-top:none}
  .headline-num{position:absolute;left:22px;top:14px;font:900 112px/1 "Montserrat",sans-serif;color:var(--forest);letter-spacing:-6px}
  .headline-unit{position:absolute;left:162px;top:78px;font:400 50px/1 "Bebas Neue",sans-serif;color:var(--rose)}
  .headline-sub{position:absolute;left:0;width:100%;top:122px;text-align:center;font:400 40px/1 "Bebas Neue",sans-serif;color:var(--rose);letter-spacing:0.5px}
  .headline-main{position:absolute;left:0;width:100%;top:186px;text-align:center;font:900 52px/1 "Montserrat",sans-serif;color:var(--white);letter-spacing:-1px}
  .headline-tail{position:absolute;left:0;width:100%;top:248px;text-align:center;font:900 40px/1 "Montserrat",sans-serif;color:var(--rose)}
  .headline-age{position:absolute;left:0;width:100%;top:290px;text-align:center;font:900 66px/1 "Montserrat",sans-serif;color:var(--rose)}

  /* Menu card */
  .menu-card{position:absolute;left:14px;top:28px;width:285px;height:320px;background:var(--rose)}
  .menu-card .dots{position:absolute;inset:9px;border:3px dotted var(--forest)}
  .menu-card .timer{position:absolute;left:110px;top:32px;width:90px;height:90px}
  .menu-line{position:absolute;left:0;width:100%;text-align:center;font-family:"Bebas Neue",sans-serif;line-height:1}
  .menu-line.light{top:130px;font-size:54px;color:var(--white)}
  .menu-line.dark-1{top:184px;font-size:54px;color:var(--forest)}
  .menu-line.dark-2{top:240px;font-size:54px;color:var(--forest)}

  /* Quote card */
  .quote-mark{position:absolute;font:700 86px/1 "Raleway",sans-serif;color:var(--blush)}
  .quote-mark.open{left:22px;top:96px}
  .quote-mark.close{right:18px;top:286px}
  .quote-text{position:absolute;left:18px;right:6px;top:162px;text-align:center;font:700 25px/1.4 "Raleway",sans-serif;color:var(--blush)}

  /* Promise card */
  .promise-box{position:absolute;left:10px;top:258px;width:288px;height:140px;background:var(--forest)}
  .promise-box .dots{position:absolute;left:9px;right:9px;top:9px;bottom:-10px;border:3px dotted var(--white)}
  .promise-text{position:absolute;left:0;width:100%;top:30px;text-align:center;font:800 29px/1.5 "Montserrat",sans-serif;color:var(--white)}
</style>
</head>
<body>
<main class="grid">

  <!-- Row 1 -->
  <section class="tile col-1 row-1">
    <div class="photo photo-portrait" role="img" aria-label="Smiling woman in a cropped white sweater pointing at her flat stomach, pink watercolor backdrop"></div>
  </section>

  <section class="tile col-2 row-1">
    <svg class="backdrop" viewBox="0 0 311 394" preserveAspectRatio="none" aria-hidden="true">
      <rect width="311" height="394" fill="var(--blush-soft)"/>
      <path d="M0 0 H230 C210 50 130 90 40 80 C15 78 0 70 0 70 Z" fill="var(--forest)"/>
      <path d="M260 0 H311 V394 H280 C300 300 250 150 290 60 Z" fill="var(--rose)" opacity="0.6"/>
    </svg>
    <div class="title-card">
      <div class="top"></div>
      <div class="bottom"></div>
      <div class="dots"></div>
      <div class="headline-num">21</div>
      <div class="headline-unit">NIGHT</div>
      <div class="headline-sub">LEAN MIDDLE</div>
      <div class="headline-main">REBOOT</div>
      <div class="headline-tail">BEYOND</div>
      <div class="headline-age">50</div>
    </div>
  </section>

  <section class="tile col-3 row-1">
    <div class="photo photo-kitchen" role="img" aria-label="Smiling woman in a cropped white sweater pointing at her waist in a modern kitchen"></div>
  </section>

  <!-- Row 2 -->
  <section class="tile col-1 row-2">
    <svg class="backdrop" viewBox="0 0 309 384" preserveAspectRatio="none">
      <rect width="309" height="384" fill="var(--blush)"/>
      <path d="M55 0 H240 C250 50 220 90 150 92 C90 94 55 60 55 0 Z" fill="#151515"/>
      <path d="M0 30 C70 40 130 90 120 150 C110 180 40 180 0 160 Z" fill="var(--forest)"/>
      <path d="M309 10 C270 40 265 90 280 120 L309 130 Z" fill="var(--forest)"/>
      <path d="M0 320 C60 330 120 350 140 384 H0 Z" fill="var(--rose)"/>
      <path d="M0 150 C90 100 260 80 309 90 V360 C230 380 110 385 30 360 C0 340 -10 250 0 150 Z" fill="#5a3b2b" role="img" aria-label="Overhead view of a meal plan notepad on a wooden table framed by fruit, vegetables, eggs and fresh meat"/>
    </svg>
  </section>

  <section class="tile col-2 row-2">
    <svg class="backdrop" viewBox="0 0 311 384" preserveAspectRatio="none" aria-hidden="true">
      <rect width="311" height="384" fill="var(--blush-soft)"/>
      <path d="M0 0 H120 C130 30 90 60 40 55 C20 53 0 45 0 45 Z" fill="var(--forest)"/>
      <path d="M311 200 V384 H160 C160 340 220 320 270 310 C300 300 300 250 311 200 Z" fill="var(--forest)"/>
      <path d="M0 190 C10 210 8 250 0 270 Z" fill="var(--rose)"/>
    </svg>
    <div class="menu-card">
      <div class="dots"></div>
      <svg class="timer" viewBox="0 0 90 90" aria-hidden="true">
        <circle cx="43" cy="47" r="38" fill="none" stroke="var(--white)" stroke-width="4"/>
        <path d="M43 2 A43 43 0 0 1 86 45 H43 Z" fill="none" stroke="var(--white)" stroke-width="4"/>
        <g stroke="var(--white)" stroke-width="3" stroke-linecap="round">
          <line x1="43" y1="14" x2="43" y2="22"/><line x1="43" y1="72" x2="43" y2="80"/>
          <line x1="10" y1="47" x2="18" y2="47"/><line x1="68" y1="47" x2="76" y2="47"/>
          <line x1="20" y1="24" x2="25" y2="29"/><line x1="20" y1="70" x2="25" y2="65"/>
          <line x1="66" y1="70" x2="61" y2="65"/>
        </g>
        <text x="40" y="57" text-anchor="middle" font-family="Bebas Neue, sans-serif" font-size="28" fill="var(--white)">20</text>
      </svg>
      <div class="menu-line light">20 SECOND</div>
      <div class="menu-line dark-1">TRIM-CORE</div>
      <div class="menu-line dark-2">MENU GUIDE</div>
    </div>
  </section>

  <section class="tile col-3 row-2">
    <svg class="backdrop" viewBox="0 0 308 384" preserveAspectRatio="none">
      <rect width="308" height="384" fill="var(--blush)"/>
      <path d="M0 50 C60 30 150 40 200 30 H308 V384 H80 C40 380 0 370 0 350 Z" fill="var(--forest)"/>
      <path d="M200 384 C230 320 280 300 308 290 V384 Z" fill="var(--rose)"/>
      <path d="M0 70 C40 45 160 35 308 40 V290 C250 310 210 340 180 352 H0 Z" fill="#6a4a36" role="img" aria-label="Table with raw chicken breasts, asparagus, berries, grapes and a meal plan sheet listing breakfast, lunch, dinner and snack"/>
    </svg>
  </section>

  <!-- Row 3 -->
  <section class="tile col-1 row-3">
    <div class="photo photo-friends" role="img" aria-label="Two women, one whispering a secret to the other who looks surprised and delighted"></div>
  </section>

  <section class="tile col-2 row-3">
    <svg class="backdrop" viewBox="0 0 311 390" preserveAspectRatio="none" aria-hidden="true">
      <rect width="311" height="390" fill="var(--blush)"/>
      <path d="M0 30 C80 10 160 30 230 60 C290 90 311 110 311 130 V390 H150 C80 340 40 360 0 330 Z" fill="var(--forest)"/>
      <path d="M170 0 H311 V45 C260 45 200 30 170 0 Z" fill="var(--forest)"/>
      <path d="M0 320 C50 330 90 360 110 390 H0 Z" fill="var(--rose)"/>
      <path d="M220 390 C240 370 280 362 305 366" fill="none" stroke="var(--white)" stroke-width="2"/>
    </svg>
    <div class="quote-mark open">&ldquo;</div>
    <p class="quote-text">Starlet Tricks to a Slender Midline Beyond 50</p>
    <div class="quote-mark close">&rdquo;</div>
  </section>

  <section class="tile col-3 row-3">
    <div class="photo photo-friends-alt" role="img" aria-label="A woman with curly hair reacts with surprise as a friend whispers in her ear"></div>
    <div class="promise-box">
      <div class="dots"></div>
      <p class="promise-text">ZERO SCALPEL<br>NEEDED</p>
    </div>
  </section>

</main>
</body>
</html>
```